wedding package brochure

We want to freshen the look for our wedding packages. Attached is a link to the current content
http://www.tarwinheadslinks.com.au/weddings/THL-Wedding-Package-2012-2013.pdf
We would like the logo (the dolphins) included and it needs to showcase the beachside location and give a classy wedding feel. I have a style guide available if required.

Industry/Entity Type

Wedding

```html
<!DOCTYPE html>
<html lang="en">
<head>
<meta charset="utf-8">
<title>About Our Venue – Wedding Package</title>
<link rel="stylesheet" href="https://fonts.googleapis.com/css2?family=Great+Vibes&family=Raleway:wght@300;400&family=Cormorant+Garamond:ital,wght@1,400&display=swap">
<style>
:root{
  --mint:#cfe9e4;
  --ink:#3b3b3b;
  --soft-ink:#555;
  --white:#ffffff;
  --sky-top:#6fb3dc;
  --sky-low:#a9d8ee;
  --sea:#4fb3c4;
  --sand:#e9e2d6;
  --beach-top:#dfeef1;
  --beach-low:#efe8df;
  --blossom:#e79ab8;
}
*{margin:0;padding:0;box-sizing:border-box}
html,body{width:1200px;height:2528px;overflow:hidden;background:var(--white)}
.brochure{position:relative;width:1200px;height:2528px;font-family:'Raleway',sans-serif;color:var(--ink)}
.venue-intro{position:absolute;left:0;top:0;width:1200px;height:848px;background:linear-gradient(180deg,var(--mint) 0%,#d9efeb 100%)}
.card{position:absolute}
.card svg{position:absolute;inset:0}
.card-content{position:relative;text-align:center}
.intro-card{left:320px;top:28px;width:864px;height:796px}
.intro-card .card-content{padding:110px 60px 0}
.section-title{font-family:'Great Vibes',cursive;font-weight:400;font-size:104px;line-height:1;color:#222;margin-bottom:160px}
.body-copy{font-size:20px;line-height:30px;font-weight:300;color:var(--soft-ink);margin-bottom:44px}
.body-copy em,.feature,.venue-name{font-family:'Cormorant Garamond',serif;font-style:italic;font-size:23px;color:var(--ink)}
.venue-name{display:block}
.couple-photo{position:absolute;left:0;top:848px;width:1200px;height:832px;background:linear-gradient(180deg,var(--sky-top) 0%,var(--sky-low) 45%,var(--sea) 70%,var(--sand) 100%)}
.photo-caption{position:absolute;left:0;top:870px;width:1200px;padding:0 30px;text-align:center;color:var(--white);font-weight:300;font-size:44px;line-height:48px}
.celebration{position:absolute;left:0;top:1680px;width:1200px;height:848px;background:linear-gradient(180deg,var(--beach-top) 0%,var(--beach-low) 100%)}
.blossom-corner{position:absolute;left:0;top:2300px;width:360px;height:228px;background:radial-gradient(ellipse at 30% 50%,var(--blossom) 0%,rgba(231,154,184,.4) 55%,rgba(231,154,184,0) 75%)}
.celebration-card{left:240px;top:1716px;width:944px;height:688px}
.celebration-card .card-content{padding:44px 60px 0}
.celebration-card .body-copy{font-size:22px;line-height:38px;margin-bottom:54px}
.underlined{text-decoration:underline;text-underline-offset:5px}
</style>
</head>
<body>
<main class="brochure">

  <section class="venue-intro" role="img" aria-label="Soft mint chevron background pattern"></section>
  <div class="card intro-card">
    <svg width="864" height="796" viewBox="0 0 864 796" aria-hidden="true">
      <path d="M80,0 H784 A80 80 0 0 0 864,80 V716 A80 80 0 0 0 784,796 H80 A80 80 0 0 0 0,716 V80 A80 80 0 0 0 80,0 Z" fill="#fff"/>
    </svg>
    <div class="card-content">
      <h1 class="section-title">About Our Venue</h1>
      <p class="body-copy">Tarwin Heads Links has two venues<br>to choose from for your upcoming wedding<br>either the <em>spectacular views of Tarwin Beach</em><br>or the <em>picturesque surrounds of Hilltop Links</em></p>
      <p class="body-copy"><span class="venue-name">At Tarwin Heads Beachside Links</span>we offer a private room &amp; adjacent terrace<br>with majestic views of Tarwin Beach.</p>
      <p class="body-copy"><span class="venue-name">At Hilltop Links</span>we offer picturesque views overlooking<br>the 18 hole championship golf course.</p>
    </div>
  </div>

  <section class="couple-photo" role="img" aria-label="Photograph of a smiling bride and groom embracing on a tropical beach"></section>
  <p class="photo-caption">Tarwin Heads is only two and half hours' drive from<br>Sydney and Canberra making it the perfect<br>wedding destination</p>

  <section class="celebration" role="img" aria-label="Soft focus beach background with sand and coral"></section>
  <div class="blossom-corner" role="img" aria-label="Pink frangipani flowers"></div>
  <div class="card celebration-card">
    <svg width="944" height="688" viewBox="0 0 944 688" aria-hidden="true">
      <path d="M80,0 H864 A80 80 0 0 0 944,80 V608 A80 80 0 0 0 864,688 H80 A80 80 0 0 0 0,608 V80 A80 80 0 0 0 80,0 Z" fill="#fff"/>
    </svg>
    <div class="card-content">
      <p class="body-copy">A wonderful venue for your wedding celebration.<br><span class="feature underlined">The Beachside or Hilltop Club House</span> has all the<br>facilities to ensure that your day is a success.</p>
      <p class="body-copy"><span class="feature underlined">The Room at Beachside</span> is filled with natural light, offering<br>spectacular views of the beach &amp; seating up to 200 guests<br>the adjoining Outdoor Terrace is<br>a more casual area for guests to relax.</p>
      <p class="body-copy">The adjoining <span class="feature underlined">Outdoor Terrace</span><br>is a more casual area for guests to relax.</p>
    </div>
  </div>

</main>
</body>
</html>
```